Continuation of "Why Choose Us" animated gif banners campaign

The original project would not allow me to select any more designs, so I started this new project so you can submit your designs and I will purchase them.

Thanks!

```html
<!DOCTYPE html>
<html lang="en">
<head>
<meta charset="UTF-8">
<title>Why Choose Us – Banner Set</title>
<link href="https://fonts.googleapis.com/css2?family=Poppins:wght@600;800&display=swap" rel="stylesheet">
<style>
  :root {
    --stage: #000000;
    --sheet: #ffffff;
    --ink: #111111;
    --line: rgba(255,255,255,0.92);
    --pink-a: #f52d93; --pink-b: #d8106f;
    --purple-a: #9047f0; --purple-b: #6a22d0;
    --red-a: #ef3a48; --red-b: #cc1f30;
    --orange-a: #f8922e; --orange-b: #e9681a;
    --yellow-a: #f7d036; --yellow-b: #e8b118;
    --green-a: #4fd24a; --green-b: #2aab2e;
    --cyan-a: #3cc8f0; --cyan-b: #1a9fd6;
    --blue-a: #3b4ef0; --blue-b: #1f2cc4;
    --brown-a: #b94848; --brown-b: #8f2c2c;
    --mauve-a: #cdb6b6; --mauve-b: #a88e8e;
    --black-a: #2a2a2a; --black-b: #050505;
  }
  * { margin: 0; padding: 0; box-sizing: border-box; }
  html, body { width: 682px; height: 1200px; overflow: hidden; background: var(--stage); }
  .sheet {
    position: absolute; left: 127px; top: 0; width: 428px; height: 1200px;
    background: var(--sheet);
  }
  .banner-list { position: absolute; left: 22px; top: 22px; width: 384px; }
  .banner {
    position: relative; width: 384px; height: 90px; margin-bottom: 13.6px;
    background: linear-gradient(100deg, var(--a) 0%, var(--b) 55%, var(--a) 100%);
    overflow: hidden;
  }
  .banner-frame {
    position: absolute; left: 11px; right: 11px; top: 8px; bottom: 15px;
    border: 2px solid var(--line);
  }
  .banner-title {
    position: absolute; left: 0; right: 0; top: 18px;
    text-align: center; color: #fff;
    font-family: "Poppins", sans-serif; font-weight: 800; font-size: 33px;
    letter-spacing: -0.5px; line-height: 44px;
    text-shadow: 0 2px 4px rgba(0,0,0,0.3);
  }
  .banner-phone {
    position: absolute; left: 126px; top: 66px; width: 132px; height: 20px;
    background: var(--sheet); color: var(--ink);
    font-family: "Poppins", sans-serif; font-weight: 600; font-size: 14px;
    line-height: 20px; text-align: center; letter-spacing: 0.4px;
  }
  .pink { --a: var(--pink-a); --b: var(--pink-b); }
  .purple { --a: var(--purple-a); --b: var(--purple-b); }
  .red { --a: var(--red-a); --b: var(--red-b); }
  .orange { --a: var(--orange-a); --b: var(--orange-b); }
  .yellow { --a: var(--yellow-a); --b: var(--yellow-b); }
  .green { --a: var(--green-a); --b: var(--green-b); }
  .cyan { --a: var(--cyan-a); --b: var(--cyan-b); }
  .blue { --a: var(--blue-a); --b: var(--blue-b); }
  .brown { --a: var(--brown-a); --b: var(--brown-b); }
  .mauve { --a: var(--mauve-a); --b: var(--mauve-b); }
  .black { --a: var(--black-a); --b: var(--black-b); }
</style>
</head>
<body>
<main class="sheet">
  <div class="banner-list">
    <section class="banner pink" role="img" aria-label="Pink banner with soft circuit-board texture"><div class="banner-frame"></div><h2 class="banner-title">WHY CHOOSE US</h2><p class="banner-phone">0198 765 4320</p></section>
    <section class="banner purple" role="img" aria-label="Purple banner with soft circuit-board texture"><div class="banner-frame"></div><h2 class="banner-title">WHY CHOOSE US</h2><p class="banner-phone">0198 765 4320</p></section>
    <section class="banner red" role="img" aria-label="Red banner with soft circuit-board texture"><div class="banner-frame"></div><h2 class="banner-title">WHY CHOOSE US</h2><p class="banner-phone">0198 765 4320</p></section>
    <section class="banner orange" role="img" aria-label="Orange banner with soft circuit-board texture"><div class="banner-frame"></div><h2 class="banner-title">WHY CHOOSE US</h2><p class="banner-phone">0198 765 4320</p></section>
    <section class="banner yellow" role="img" aria-label="Yellow banner with soft circuit-board texture"><div class="banner-frame"></div><h2 class="banner-title">WHY CHOOSE US</h2><p class="banner-phone">0198 765 4320</p></section>
    <section class="banner green" role="img" aria-label="Green banner with soft circuit-board texture"><div class="banner-frame"></div><h2 class="banner-title">WHY CHOOSE US</h2><p class="banner-phone">0198 765 4320</p></section>
    <section class="banner cyan" role="img" aria-label="Cyan banner with soft circuit-board texture"><div class="banner-frame"></div><h2 class="banner-title">WHY CHOOSE US</h2><p class="banner-phone">0198 765 4320</p></section>
    <section class="banner blue" role="img" aria-label="Blue banner with soft circuit-board texture"><div class="banner-frame"></div><h2 class="banner-title">WHY CHOOSE US</h2><p class="banner-phone">0198 765 4320</p></section>
    <section class="banner brown" role="img" aria-label="Brown banner with soft circuit-board texture"><div class="banner-frame"></div><h2 class="banner-title">WHY CHOOSE US</h2><p class="banner-phone">0198 765 4320</p></section>
    <section class="banner mauve" role="img" aria-label="Mauve banner with soft circuit-board texture"><div class="banner-frame"></div><h2 class="banner-title">WHY CHOOSE US</h2><p class="banner-phone">0198 765 4320</p></section>
    <section class="banner black" role="img" aria-label="Black banner with soft circuit-board texture"><div class="banner-frame"></div><h2 class="banner-title">WHY CHOOSE US</h2><p class="banner-phone">0198 765 4320</p></section>
  </div>
</main>
</body>
</html>
```